Dean harlowe realestate

We want something complete different to our website now and something that will stand out this is our website http://deanharlowerealestate-demo.com/

our company website for my boss is www.stevenorrick-demo.com

please note this website is being made for dean harlowe not steven orrick

something similar to our company website but has to be in the branding of dean harlowe realestate

```html
<!DOCTYPE html>
<html lang="en">
<head>
<meta charset="utf-8">
<title>Dean Harlowe Property</title>
<link href="https://fonts.googleapis.com/css2?family=Open+Sans:ital,wght@0,300;0,400;0,600;0,700;1,400&family=Oswald:wght@500&display=swap" rel="stylesheet">
<style>
:root{
  --navy:#1b1682;
  --navy-dark:#15106a;
  --red:#e5121b;
  --maroon:#7b1022;
  --orange:#f58a2a;
  --ink:#222;
  --wood:#3b302c;
  --white:#fff;
}
*{margin:0;padding:0;box-sizing:border-box}
html,body{width:686px;height:1200px;overflow:hidden;background:#fff}
body{font-family:"Open Sans",Arial,sans-serif;color:var(--ink)}
.page{position:relative;width:686px;height:1200px;overflow:hidden}
.abs{position:absolute}

/* header */
.brand{left:63px;top:19px;width:235px;height:34px;border-top:2px solid #555;border-bottom:2px solid #555;background:linear-gradient(90deg,#ececec,#f8f8f8,#ececec);display:flex;align-items:center;justify-content:center;font-size:17px;font-weight:300;color:#222}
.call{left:473px;top:8px;font-size:6px;font-weight:700;color:var(--red)}
.call strong{display:block;font-size:11px;font-weight:400;color:var(--navy);margin-top:1px}
.follow{left:565px;top:8px;font-size:6px;font-weight:700;color:var(--red)}
.dots{display:flex;gap:2px;margin-top:3px}
.dots i{width:10px;height:10px;border-radius:50%;display:block}
.nav{left:337px;top:37px;width:349px;height:25px;background:linear-gradient(#f5131c,#d80f18);display:flex;align-items:center}
.nav a{color:#fff;text-decoration:none;font-size:8.5px;font-weight:700;padding:0 8px}
.nav a.home{background:var(--navy);height:25px;display:flex;align-items:center;padding:0 15px;border-radius:13px 0 0 13px;margin-right:2px}

.hero{left:0;top:73px;width:686px;height:279px;
  background:
    radial-gradient(ellipse 120px 90px at 440px 150px,rgba(40,140,255,.75),rgba(40,140,255,0) 100%),
    radial-gradient(ellipse 90px 70px at 560px 190px,rgba(30,120,255,.7),rgba(30,120,255,0) 100%),
    radial-gradient(ellipse 170px 140px at 180px 150px,#2f4670,rgba(47,70,112,0) 100%),
    linear-gradient(180deg,rgba(0,0,0,0) 55%,rgba(10,25,50,.55) 100%),
    linear-gradient(90deg,#1b2a48 0%,#243a62 30%,#5f7fa8 52%,#b9a07c 70%,#8aa6c4 84%,#2c5a92 100%)}

/* video + form */
.video{left:94px;top:360px;width:306px;height:182px;background:#2b2b33}
.screen{left:12px;top:9px;width:282px;height:126px;background:
  linear-gradient(180deg,rgba(255,255,255,.9) 0%,rgba(255,255,255,.2) 45%,rgba(255,255,255,.5) 100%),
  linear-gradient(90deg,#cfd3dc 0%,#aeb4c0 20%,#e6e8ec 35%,#b8bdc8 55%,#eceef1 70%,#a9afbb 88%,#d9dce2 100%)}
.screen p{position:absolute;left:100px;top:48px;font-family:Arial,sans-serif;font-weight:700;color:#e0661c;font-size:14px;line-height:16px}
.screen p span{display:block;padding-left:28px}
.bar{left:12px;top:128px;width:282px;height:7px;background:#2d2d33}
.callbtn{left:94px;top:143px;width:154px;height:36px}
.callbtn .pill{left:18px;top:4px;width:132px;height:28px;background:linear-gradient(#f11a22,#b40c14);border-radius:0 8px 8px 0;color:#fff;font-size:12.5px;display:flex;align-items:center;padding-left:28px}
.callbtn .disc{left:0;top:0;width:36px;height:36px;border-radius:50%;background:var(--navy-dark);border:2px solid var(--red);display:flex;align-items:center;justify-content:center}

.appraisal{left:417px;top:360px;width:175px;height:182px;background:var(--navy);border-radius:5px}
.appraisal h2{position:absolute;left:0;width:175px;top:10px;text-align:center;color:#fff;font-size:10.5px;font-weight:400}
.field{position:absolute;left:20px;width:136px;height:17px;background:#fff;border-radius:2px;font-size:6px;color:#333;padding:5px 8px}
.send{left:46px;top:159px;width:86px;height:23px}
.send span{position:absolute;inset:0;display:flex;align-items:center;justify-content:center;color:#fff;font-size:10px}

/* sold */
.sold-band{left:0;top:551px;width:686px;height:288px;background:linear-gradient(135deg,#fafafa,#e9e9ec 50%,#f7f7f8);border-top:1px solid #e2e2e2;border-bottom:1px solid #e2e2e2}
.title{position:absolute;left:0;width:686px;text-align:center;font-size:13px;font-weight:700;color:var(--maroon)}
.title b{color:var(--navy)}
.card{position:absolute;width:157px;height:100px;background:#fff;box-shadow:0 1px 4px rgba(0,0,0,.3);border-radius:3px;overflow:hidden}
.card .photo{height:77px}
.p1{background:linear-gradient(180deg,#7ea3d4 0%,#b9cde6 30%,#c46a5c 42%,#b8aa98 58%,#c47a5a 78%,#9c5a44 100%)}
.p2{background:linear-gradient(180deg,#3a4d6e 0%,#5d7a5a 25%,#e8dcc0 45%,#d08a3a 62%,#3e6a32 80%,#2d3a24 100%)}
.p3{background:linear-gradient(180deg,#6b95cc 0%,#a9c3e3 28%,#a0584a 42%,#c8a48c 58%,#6c8a4a 76%,#b87a5e 100%)}
.p4{background:linear-gradient(180deg,#9cb8dc 0%,#c8d6e6 25%,#8a8a8a 35%,#d6cfc2 50%,#c8c2b4 75%,#7ea24c 100%)}
.p5{background:linear-gradient(180deg,#4a7cc8 0%,#8cb0e0 40%,#c86e4a 55%,#d0c4aa 68%,#8a6a52 82%,#9c8e7a 100%)}
.p6{background:linear-gradient(180deg,#4d86d6 0%,#93b9e6 30%,#c8785c 42%,#ecd9b8 58%,#e2d2b0 78%,#a6a08c 100%)}
.card .tag{position:absolute;right:0;top:5px;background:var(--red);color:#fff;font-size:5.5px;font-weight:700;padding:1px 8px}
.card .cap{position:absolute;left:0;top:76px;width:157px;height:24px;padding:2px 6px;font-size:8px;line-height:10px;color:var(--maroon);font-weight:600}
.card .cap span{display:block;color:var(--navy)}
.card.active .cap{background:var(--red);color:#fff;top:72px;height:28px;padding-top:5px}
.card.active .cap span{color:#fff}
.pager{left:280px;top:807px;display:flex;box-shadow:0 1px 3px rgba(0,0,0,.3)}
.pager span{width:21px;height:23px;background:#fff;border:1px solid #ddd;font-size:8px;color:#4a7ab8;display:flex;align-items:center;justify-content:center}
.pager span.on{background:var(--orange);color:#fff;border-color:var(--orange)}

/* testimonials */
.quote{position:absolute;top:876px;width:260px;height:70px}
.quote .mark{position:absolute;left:0;top:5px;font-size:18px;font-weight:700;color:#777;line-height:12px}
.avatar{position:absolute;left:15px;top:5px;width:56px;height:56px;border-radius:50%;border:2px solid #333;background:linear-gradient(#d8dee6,#9aa8b8)}
.quote p{position:absolute;left:84px;top:5px;width:124px;font-size:6.2px;line-height:8.2px;font-style:italic}
.quote .who{position:absolute;left:84px;top:50px;font-size:5.5px;font-weight:700}
.quote .who em{font-style:normal;color:var(--red);font-size:8px;margin-left:4px}
.divider{left:342px;top:873px;width:1px;height:68px;background:#ddd}
.slider{left:331px;top:956px;display:flex;gap:3px}
.slider i{width:5px;height:5px;border-radius:50%;background:#888;display:block}
.slider i.on{background:var(--navy)}

/* map + footer */
.mapwrap{left:0;top:976px;width:686px;height:124px}
.footer{left:0;top:1095px;width:686px;height:88px;background:linear-gradient(90deg,#3a2f2b,#4a3d37 50%,#3a2f2b)}
.footer{color:#fff}
.col{position:absolute;top:2px}
.col h3{font-family:"Oswald",Arial,sans-serif;font-weight:500;font-size:10px;line-height:13px;border-bottom:1px solid #fff;display:inline-block;margin-bottom:2px}
.links li{list-style:none;font-size:7.3px;line-height:10px}
.contact p{font-size:6.5px;line-height:7.6px;padding-left:12px;position:relative;margin-bottom:3px}
.contact p svg{position:absolute;left:0;top:1px}
.news p{font-size:7.3px;line-height:8.5px;margin-bottom:3px}
.news .in{width:78px;height:10px;border:1px solid #ccc;font-size:5.5px;padding:1px 5px;margin-bottom:3px;line-height:7px}
.news .btn{width:78px;height:11px;background:#fff;color:var(--navy);font-size:6.5px;font-weight:700;text-align:center;line-height:11px}
.soc{display:grid;grid-template-columns:repeat(4,10px);gap:4px;margin-top:3px}
.soc i{width:10px;height:10px;border-radius:50%;display:block}
.copy{left:0;top:1183px;width:686px;height:17px;background:var(--navy-dark);color:#fff;font-size:6px;font-weight:600;padding:5px 0 0 96px}
</style>
</head>
<body>
<div class="page">

  <header>
    <div class="abs brand">Dean Harlowe Property</div>
    <div class="abs call">CALL US NOW<strong>0400 555 018</strong></div>
    <div class="abs follow">FOLLOW US ON
      <div class="dots"><i style="background:#3b5998"></i><i style="background:#e52d27"></i><i style="background:#1da1f2"></i><i style="background:#4a76a8"></i></div>
    </div>
    <nav class="abs nav">
      <a class="home" href="#">HOME</a><a href="#">FOR SALE</a><a href="#">AGENTS</a><a href="#">BOOK APPRAISAL</a><a href="#">CONTACT</a>
    </nav>
  </header>

  <div class="abs hero" role="img" aria-label="Hero photo: agent in a suit holding a tablet with glowing blue hexagons over a blurred city skyline"></div>

  <section class="abs video">
    <div class="abs screen" role="img" aria-label="Video thumbnail of a hazy city skyline">
      <p>MARKET<span>UPDATE</span></p>
    </div>
    <div class="abs bar"></div>
    <div class="abs callbtn">
      <div class="abs pill">0400 555 018</div>
      <div class="abs disc">
        <svg width="16" height="16" viewBox="0 0 24 24"><path fill="#fff" d="M6.6 10.8a15 15 0 0 0 6.6 6.6l2.2-2.2a1 1 0 0 1 1-.25 11.4 11.4 0 0 0 3.6.57 1 1 0 0 1 1 1V20a1 1 0 0 1-1 1A17 17 0 0 1 3 4a1 1 0 0 1 1-1h3.5a1 1 0 0 1 1 1c0 1.25.2 2.45.57 3.57a1 1 0 0 1-.25 1z"/></svg>
      </div>
    </div>
  </section>

  <section class="abs appraisal">
    <h2>BOOK AN APPRAISAL</h2>
    <div class="field" style="top:32px">Name</div>
    <div class="field" style="top:51px">Email</div>
    <div class="field" style="top:70px">Phone</div>
    <div class="field" style="top:89px">Address</div>
    <div class="field" style="top:108px">Prefered Time/Day</div>
    <div class="field" style="top:126px;height:30px;padding-top:4px">Message</div>
    <div class="abs send">
      <svg width="86" height="23" viewBox="0 0 86 23"><path d="M6 0H80L86 23H0Z" fill="#fff"/><path d="M8 2H78L83 23H3Z" fill="#e5121b"/></svg>
      <span>SEND</span>
    </div>
  </section>

  <section class="abs sold-band"></section>
  <h2 class="title" style="top:562px">LATEST <b>PROPERTIES SOLD</b></h2>

  <div class="card" style="left:96px;top:586px"><div class="photo p1" role="img" aria-label="Brick home with red tiled roof and paved driveway"></div><div class="tag">SOLD</div><div class="cap">44 WRENMORE STREET<span>ASHVALE, 6190</span></div></div>
  <div class="card active" style="left:266px;top:586px"><div class="photo p2" role="img" aria-label="Two-storey home with lit garden at dusk"></div><div class="tag">SOLD</div><div class="cap">19 CORBEL STREET<span>LINFIELD,&nbsp; 6191</span></div></div>
  <div class="card" style="left:436px;top:586px"><div class="photo p3" role="img" aria-label="Brick home with front garden"></div><div class="tag">SOLD</div><div class="cap">65 TALLIS&nbsp; STREET<span>ASHVALE, 6190</span></div></div>
  <div class="card" style="left:96px;top:699px"><div class="photo p4" role="img" aria-label="Rendered home with double garage"></div><div class="tag">SOLD</div><div class="cap">21 PEMBERLY STREET<span>ASHVALE, 6190</span></div></div>
  <div class="card" style="left:266px;top:699px"><div class="photo p5" role="img" aria-label="Low brick home behind a front fence"></div><div class="tag">SOLD</div><div class="cap">80a DUNMORE STREET<span>ASHVALE, 6190</span></div></div>
  <div class="card" style="left:436px;top:699px"><div class="photo p6" role="img" aria-label="Cream home with tiled roof and pillared fence"></div><div class="tag">SOLD</div><div class="cap">387 HALFORD AVENUE<span>ASHVALE, 6190</span></div></div>

  <div class="abs pager"><span class="on">1</span><span>2</span><span>3</span><span>4</span><span>5</span><span>»</span></div>

  <h2 class="title" style="top:847px">WHAT <b>CLIENTS</b> SAY ABOUT US</h2>
  <div class="quote" style="left:96px">
    <div class="mark">“</div>
    <div class="avatar" role="img" aria-label="Client portrait"></div>
    <p>"We bought our first home through process was easy and very straight We felt confident buying our first home We put a few offers forward on other proper that piece of mind that we felt with Dean."</p>
    <div class="who">Marla &amp; Tobin<em>★★★★★</em></div>
  </div>
  <div class="abs divider"></div>
  <div class="quote" style="left:388px">
    <div class="mark">“</div>
    <div class="avatar" role="img" aria-label="Client portrait"></div>
    <p>"We bought our first home through process was easy and very straight We felt confident buying our first home We put a few offers forward on other proper that piece of mind that we felt with Dean."</p>
    <div class="who">Greg Castell<em>★★★★★</em></div>
  </div>
  <div class="abs slider"><i></i><i class="on"></i><i></i></div>

  <div class="abs mapwrap">
    <svg width="686" height="124" viewBox="0 0 686 124">
      <defs>
        <linearGradient id="mapTone" x1="0" y1="0" x2="1" y2="1">
          <stop offset="0" stop-color="#dfe6dc"/><stop offset=".3" stop-color="#ecebe4"/>
          <stop offset=".55" stop-color="#f2edd6"/><stop offset=".8" stop-color="#e7e9ec"/><stop offset="1" stop-color="#d9e2ec"/>
        </linearGradient>
      </defs>
      <rect width="686" height="124" fill="url(#mapTone)" role="img" aria-label="Street map around the office location"/>
      <path d="M0 84Q343 138 686 84V124H0Z" fill="#3b302c"/>
      <path d="M0 84Q343 138 686 84" fill="none" stroke="#fff" stroke-width="1.5"/>
      <path d="M0 88Q343 142 686 88" fill="none" stroke="#7b1022" stroke-width="5"/>
      <path d="M394 80c-3 0-5 2-5 5 0 4 5 9 5 9s5-5 5-9c0-3-2-5-5-5z" fill="#e5121b"/>
      <circle cx="394" cy="85" r="1.8" fill="#fff"/>
    </svg>
  </div>

  <footer class="abs footer">
    <div class="col" style="left:96px">
      <h3>Quick Links</h3>
      <ul class="links"><li>› Home</li><li>› For Slae</li><li>› Agents</li><li>› Book Appraisal</li><li>› Contacts</li><li>› Privacy</li></ul>
    </div>
    <div class="col contact" style="left:221px">
      <h3>Contact Us</h3>
      <p><svg width="8" height="10" viewBox="0 0 8 10"><path d="M4 0a4 4 0 0 1 4 4c0 3-4 6-4 6S0 7 0 4a4 4 0 0 1 4-4z" fill="#fff"/><circle cx="4" cy="4" r="1.5" fill="#3b302c"/></svg>ADDRESS<br>Suite 12, 40 Larkfield Road,<br>Westmere, WA 6199 Australia</p>
      <p><svg width="9" height="9" viewBox="0 0 24 24"><path fill="#fff" d="M6.6 10.8a15 15 0 0 0 6.6 6.6l2.2-2.2a1 1 0 0 1 1-.25 11.4 11.4 0 0 0 3.6.57 1 1 0 0 1 1 1V20a1 1 0 0 1-1 1A17 17 0 0 1 3 4a1 1 0 0 1 1-1h3.5a1 1 0 0 1 1 1c0 1.25.2 2.45.57 3.57a1 1 0 0 1-.25 1z"/></svg>Call Us<br>0400 555 018</p>
      <p><svg width="9" height="7" viewBox="0 0 9 7"><rect width="9" height="7" fill="#fff"/><path d="M0 0l4.5 4L9 0" fill="none" stroke="#3b302c"/></svg>Email<br>dean@stevenorrick-demo.com</p>
    </div>
    <div class="col news" style="left:381px">
      <h3>Newsletter</h3>
      <p>Get Tips by subcribing<br>to our monthly newsletter</p>
      <div class="in">Name</div>
      <div class="in">Email</div>
      <div class="btn">Subscribe Now</div>
    </div>
    <div class="col" style="left:539px">
      <h3>Follow Us</h3>
      <div class="soc"><i style="background:#e52d27"></i><i style="background:#4a76a8"></i><i style="background:#dd4b39"></i><i style="background:#35465c"></i><i style="background:#1da1f2"></i><i style="background:#3b5998"></i><i style="background:#c13584"></i><i style="background:#2d8cff"></i></div>
    </div>
  </footer>
  <div class="abs copy">© Copyright&nbsp; 2018 https://www.deanharlowerealestate-demo.com/ All rights reserved.</div>

</div>
</body>
</html>
```